Healthy Meal Delivery Website needs a new face lift

Hi there,

The current website i have is super old and outdated.

I would like a beautiful modern site that has all the same content as the previous except with a a new, modern and trustworthy feel.

The current website is http://www.brightplate.ca/

Target Market(s)

Diet Meal delivery, weight loss, healthy meal delivery

Industry/Entity Type

Food Service

Number of Pages Required

5+ page

Font styles to use
Sans Serif

Requirements
Must have
• Modern & Clean
Should not have
• Anything outdated or cheesy

```html
<!DOCTYPE html>
<html lang="en">
<head>
<meta charset="utf-8">
<title>BrightPlate Delivery – Fresh Diet Meals Delivered</title>
<link href="https://fonts.googleapis.com/css2?family=Cinzel:wght@400;700&family=Open+Sans:wght@400;600;700&display=swap" rel="stylesheet">
<style>
:root{
  --accent:#29b6e6;
  --ink:#1d1d1d;
  --text:#444;
  --muted:#777;
  --hero-bg:#f2f3f5;
  --white:#fff;
  --footer:#262222;
  --bar:#111;
}
*{box-sizing:border-box;margin:0;padding:0}
html,body{width:1200px;height:3782px;overflow:hidden}
body{position:relative;font-family:"Open Sans",sans-serif;color:var(--text);background:var(--white)}
.abs{position:absolute}
.serif{font-family:"Cinzel",serif}
.btn{position:absolute;display:flex;align-items:center;justify-content:center;background:var(--bar);color:var(--white);font-weight:700;font-size:15px;letter-spacing:1.5px;border-radius:24px;text-transform:uppercase}
.ph{position:absolute}

/* header */
.logo{left:108px;top:28px;font-size:32px;font-weight:700;color:var(--accent);display:flex;align-items:center;gap:10px}
.logo .mark{width:22px;height:22px;border-radius:50%;background:var(--accent)}
.top-contact{top:28px;left:545px;display:flex;gap:30px;font-size:13px;color:var(--text);align-items:center;white-space:nowrap}
.top-contact span{display:flex;align-items:center;gap:8px}
.ico{width:26px;height:26px;border:1.5px solid var(--accent);border-radius:50%;display:inline-flex;align-items:center;justify-content:center}
.auth{top:26px;left:880px;display:flex;gap:18px}
.auth span{height:30px;padding:0 20px;border-radius:15px;font-size:12px;font-weight:700;display:flex;align-items:center;letter-spacing:1px}
.signup{border:1.5px solid var(--accent);color:var(--accent);background:var(--white)}
.login{background:var(--accent);color:var(--white)}
.nav{top:80px;left:403px;display:flex;gap:6px;font-size:13px;font-weight:700;color:var(--ink);white-space:nowrap}
.nav span{padding:7px 16px;border-radius:16px}
.nav .on{background:var(--accent);color:var(--white)}

/* hero */
.hero{left:0;top:0;width:1200px;height:600px;background:var(--hero-bg)}
.hero-title{left:144px;top:182px;font-size:37px;line-height:48px;color:var(--accent);letter-spacing:1px;white-space:nowrap}
.hero-sub{left:144px;top:282px;font-size:28px;line-height:36px;color:#555;width:400px}
.dots{left:142px;top:464px;display:flex;gap:10px}
.dots i{width:11px;height:11px;border:1.5px solid #777;border-radius:50%;display:block}
.dots i.on{border-color:var(--accent);background:var(--accent)}

/* features */
.features{left:144px;top:517px;width:914px;height:152px;background:var(--white);box-shadow:0 4px 18px rgba(0,0,0,.12);display:grid;grid-template-columns:repeat(6,1fr);padding:26px 10px}
.feature{text-align:center}
.feature svg{display:block;margin:0 auto 8px}
.feature h4{font-size:12px;letter-spacing:1px;color:var(--ink);font-weight:700;white-space:nowrap}
.feature p{font-size:10px;color:var(--muted);line-height:14px;margin-top:4px;padding:0 10px}

/* about */
.about-kicker{left:527px;top:776px;font-size:20px;letter-spacing:1px;color:var(--ink);white-space:nowrap}
.about-title{left:527px;top:806px;font-size:29px;color:var(--accent);letter-spacing:1px;white-space:nowrap}
.about-copy{left:527px;top:865px;width:490px;font-size:14px;line-height:28px;color:#333}

/* program */
.program{left:0;top:1164px;width:1200px;height:666px;background:linear-gradient(135deg,#3a3430,#6b5d52 50%,#2e2a27)}
.program-shade{left:0;top:1164px;width:1200px;height:666px;background:rgba(0,0,0,.45)}
.program-title{left:0;top:1262px;width:1200px;text-align:center;font-size:34px;color:var(--white);letter-spacing:2px}
.card{left:540px;top:1381px;width:481px;height:302px;background:var(--white);padding:40px 45px}
.card h3{font-family:"Cinzel",serif;font-size:24px;color:var(--accent);font-weight:400;letter-spacing:1px}
.card p{font-size:13px;line-height:26px;color:#333;margin-top:14px}
.arrows{left:965px;top:1640px;display:flex;gap:8px}

/* delivery */
.delivery-title{left:0;top:1925px;width:1200px;text-align:center;font-size:34px;color:var(--ink);letter-spacing:1px}
.tabs{left:160px;top:2030px;width:880px;display:flex;justify-content:space-between;font-size:15px;color:#333}
.tabs .on{color:var(--accent);font-weight:600}
.delivery-copy{left:178px;top:2140px;width:420px;font-size:13px;line-height:26px;color:#333}

/* testimonials */
.testi-bg{left:0;top:2495px;width:1200px;height:458px;background:#f6f6f6}
.testi-title{left:555px;top:2573px;width:540px;text-align:center;font-size:34px;color:var(--ink);letter-spacing:1px;white-space:nowrap}
.avatar{left:782px;top:2644px;width:86px;height:86px;border-radius:50%;background:linear-gradient(#d9b27a,#b07f4f);border:3px solid var(--white)}
.testi-name{left:555px;top:2742px;width:540px;text-align:center;font-size:17px;color:var(--ink);letter-spacing:1px}
.testi-role{left:555px;top:2766px;width:540px;text-align:center;font-size:12px;font-weight:700;color:var(--ink)}
.testi-quote{left:595px;top:2792px;width:460px;text-align:center;font-size:16px;line-height:30px;color:#888;font-style:italic}

/* questions */
.q-title{left:447px;top:3070px;width:600px;text-align:right;font-size:38px;color:var(--accent);letter-spacing:1.5px;white-space:nowrap}
.q-mail{left:447px;top:3142px;width:600px;text-align:right;font-size:19px;color:#222;white-space:nowrap}

/* footer */
.footer{left:0;top:3360px;width:1200px;height:375px;background:var(--footer)}
.f-head{top:3435px;font-size:14px;font-weight:700;color:var(--white);letter-spacing:1px;white-space:nowrap}
.f-about{left:108px;top:3490px;width:270px;font-size:11px;line-height:17px;color:#ccc}
.f-love{left:108px;top:3612px;font-size:11px;color:#ccc}
.f-love b{color:var(--accent);font-weight:400}
.f-team{left:108px;top:3640px;font-size:14px;color:var(--white);letter-spacing:1px}
.f-links{left:436px;top:3490px;list-style:none;font-size:11px;line-height:25px;color:#ccc}
.f-links li::before{content:"";display:inline-block;width:5px;height:5px;border-radius:50%;background:var(--accent);margin-right:12px;vertical-align:middle}
.f-contact{left:612px;top:3490px;width:230px;font-size:11px;line-height:16px;color:#ccc}
.f-contact b{color:var(--white);display:block;margin:4px 0}
.f-row{display:flex;gap:8px;margin-bottom:8px}
.f-row i{width:10px;height:10px;border-radius:50%;background:var(--accent);flex:none;margin-top:3px}
.inq{left:865px;width:228px;height:28px;border:1px solid #666;font-size:11px;color:#ccc;padding:6px 8px}
.inq-btn{left:865px;top:3625px;width:138px;height:30px;background:var(--accent);color:var(--white);font-size:11px;font-weight:700;letter-spacing:1px;border-radius:15px;display:flex;align-items:center;justify-content:center}
.bottom{left:0;top:3735px;width:1200px;height:47px;background:var(--bar);color:#bbb;font-size:11px;padding:16px 108px}
.share{top:3747px;display:flex;gap:6px;left:982px}
.share span{background:#4a67a8;color:var(--white);font-size:11px;font-weight:700;padding:3px 10px;border-radius:2px}
</style>
</head>
<body>

<section class="hero abs" aria-label="Hero"></section>
<div class="ph" role="img" aria-label="Smiling woman holding a knife and fork behind a plate with a wrap" style="left:517px;top:113px;width:516px;height:404px;background:linear-gradient(180deg,#ece4df,#c9443c 70%,#e9e7e5)"></div>

<header>
  <div class="logo abs"><span class="mark"></span>BrightPlate</div>
  <div class="top-contact abs">
    <span><i class="ico"><svg width="12" height="12" viewBox="0 0 24 24"><path d="M6.6 10.8a15 15 0 0 0 6.6 6.6l2.2-2.2a1 1 0 0 1 1-.25 11.4 11.4 0 0 0 3.6.57 1 1 0 0 1 1 1V20a1 1 0 0 1-1 1A17 17 0 0 1 3 4a1 1 0 0 1 1-1h3.5a1 1 0 0 1 1 1c0 1.25.2 2.45.57 3.57a1 1 0 0 1-.25 1z" fill="#29b6e6"/></svg></i>416-555-0142</span>
    <span><i class="ico"><svg width="12" height="10" viewBox="0 0 24 18"><rect x="1" y="1" width="22" height="16" fill="none" stroke="#29b6e6" stroke-width="2"/><path d="M1 1l11 9 11-9" fill="none" stroke="#29b6e6" stroke-width="2"/></svg></i>hello@brightplate.ca</span>
  </div>
  <div class="auth abs"><span class="signup">SIGN UP</span><span class="login">LOGIN</span></div>
  <nav class="nav abs">
    <span class="on">HOME</span><span>HOW IT WORKS</span><span>PRICING</span><span>SAMPLE MENU</span><span>CELEBRITY</span><span>F.A.Q.</span><span>CONTACT US</span>
  </nav>
</header>

<h1 class="hero-title abs serif">Fresh diet<br>meals delivered</h1>
<p class="hero-sub abs">Providing Toronto Diet Meal Delivery For 15 Years.</p>
<div class="btn" style="left:144px;top:378px;width:176px;height:42px">Get Started</div>
<div class="dots abs"><i></i><i class="on"></i><i></i><i></i></div>

<div class="features abs">
  <div class="feature"><svg width="30" height="30" viewBox="0 0 30 30" fill="none" stroke="#29b6e6" stroke-width="2"><path d="M4 13h5v13H4zM9 24l5 2h9l3-11h-8l1-7-3-1-7 8"/></svg><h4>BENEFITS</h4><p>Fresh diet meal delivery daily</p></div>
  <div class="feature"><svg width="30" height="30" viewBox="0 0 30 30" fill="none" stroke="#29b6e6" stroke-width="2"><rect x="6" y="4" width="18" height="22"/><path d="M10 10h10M10 15h10M10 20h6"/></svg><h4>MENU</h4><p>Inspired fresh gourmet Balance Diet meals</p></div>
  <div class="feature"><svg width="30" height="30" viewBox="0 0 30 30" fill="none" stroke="#29b6e6" stroke-width="2"><rect x="4" y="7" width="22" height="19"/><path d="M4 12h22M10 4v6M20 4v6"/></svg><h4>VARIETY</h4><p>60 Day Menu Rotation</p></div>
  <div class="feature"><svg width="30" height="30" viewBox="0 0 30 30" fill="none" stroke="#29b6e6" stroke-width="2"><circle cx="15" cy="15" r="5"/><path d="M15 3v5M15 22v5M3 15h5M22 15h5M7 7l3 3M20 20l3 3M7 23l3-3M20 10l3-3"/></svg><h4>CUSTOMIZATION</h4><p>Every fresh Balance Diet meal is personally customized</p></div>
  <div class="feature"><svg width="30" height="30" viewBox="0 0 30 30" fill="none" stroke="#29b6e6" stroke-width="2"><path d="M3 8h15v13H3zM18 12h5l4 5v4h-9"/><circle cx="8" cy="23" r="2.5"/><circle cx="22" cy="23" r="2.5"/></svg><h4>DELIVERY</h4><p>Fresh diet meal delivery daily Toronto &amp; Canada wide</p></div>
  <div class="feature"><svg width="30" height="30" viewBox="0 0 30 30" fill="none" stroke="#29b6e6" stroke-width="2"><circle cx="15" cy="11" r="6"/><path d="M5 27c1-6 5-9 10-9s9 3 10 9"/></svg><h4>CUSTOMER SERVICE</h4><p>Fresh diet meal delivery daily Toronto &amp; Canada wide</p></div>
</div>

<div class="ph" role="img" aria-label="Courier in a cap and blue shirt knocking on a red front door with a red delivery bag" style="left:144px;top:756px;width:350px;height:310px;background:linear-gradient(90deg,#6b7c72 0%,#c8cfc8 30%,#d1252a 45%,#b81d22 100%)"></div>
<p class="about-kicker abs">FRESH DIET GOURMET MEALS</p>
<h2 class="about-title abs serif">DELIVERED BY BRIGHTPLATE</h2>
<p class="about-copy abs">Fresh diet meal delivery Toronto and Canada wide is our signature fresh gourmet diet meal delivery program designed for healthy living &amp; weight loss management. Diet meal delivery Toronto has a creative gourmet menu that uses exotic flavors and ingredients to enhance your dining experience.</p>
<div class="btn" style="left:527px;top:1025px;width:176px;height:42px">Order Now</div>

<div class="program abs" role="img" aria-label="Blurred close-up of grilled chicken with greens"></div>
<div class="program-shade abs"></div>
<h2 class="program-title abs serif">PROGRAM DETAILS</h2>
<div class="ph" role="img" aria-label="Chicken and vegetable tortilla wraps on a white plate" style="left:144px;top:1343px;width:456px;height:378px;background:linear-gradient(135deg,#f4f1ea,#e3c08b 40%,#7fa843 65%,#f2efe9)"></div>
<div class="card abs">
  <h3>CUSTOMIZED FOR YOU</h3>
  <p>You are welcome to pause and restart your meal program at anytime. Our customers lead busy lives, therefore if you need to post-pone a delivery let us know with at least 48 Hours notice prior to your delivery.</p>
</div>
<div class="btn" style="left:585px;top:1593px;width:176px;height:42px">Order Now</div>
<div class="arrows abs">
  <svg width="16" height="24" viewBox="0 0 16 24"><path d="M12 3L4 12l8 9" fill="none" stroke="#111" stroke-width="3"/></svg>
  <svg width="16" height="24" viewBox="0 0 16 24"><path d="M4 3l8 9-8 9" fill="none" stroke="#29b6e6" stroke-width="3"/></svg>
</div>

<h2 class="delivery-title abs serif">Delivery System</h2>
<div class="tabs abs"><span>What's In Your Bag?</span><span class="on">Your Daily Menu</span><span>Recyclable Containers</span><span>Returning Your Cooler</span></div>
<svg class="abs" style="left:178px;top:2064px" width="848" height="30" viewBox="0 0 848 30">
  <line x1="0" y1="15" x2="848" y2="15" stroke="#888" stroke-width="1.5"/>
  <circle cx="62" cy="15" r="8" fill="#fff" stroke="#555" stroke-width="1.5"/>
  <circle cx="292" cy="15" r="10" fill="#fff" stroke="#555" stroke-width="1.5"/>
  <circle cx="292" cy="15" r="6" fill="#29b6e6"/>
  <circle cx="538" cy="15" r="8" fill="#fff" stroke="#555" stroke-width="1.5"/>
  <circle cx="785" cy="15" r="8" fill="#fff" stroke="#555" stroke-width="1.5"/>
</svg>
<p class="delivery-copy abs">You will receive your full days menu with a description of the meals, simple heating instructions and directions if the meal should be served chilled or heated. This will all be located on the front of the Cooler Bag. Any substitutions will be noted and labels are placed on your individual meal containers.</p>
<div class="ph" role="img" aria-label="Grilled chicken and vegetables in a foil meal container" style="left:731px;top:2105px;width:277px;height:215px;border-radius:40px;background:radial-gradient(ellipse at center,#9a6b3a 0%,#5d7b34 40%,#c8cbcd 62%,#fff 72%)"></div>
<div class="btn" style="left:510px;top:2348px;width:176px;height:42px">Order Now</div>

<div class="testi-bg abs"></div>
<div class="ph" role="img" aria-label="Slice of layered lasagna with tomato sauce on a white plate" style="left:0;top:2495px;width:555px;height:458px;background:linear-gradient(90deg,#b43a1e,#d9763f 45%,#f1d7b4 75%,#f6f6f6)"></div>
<h2 class="testi-title abs serif">Customer Testimonials</h2>
<div class="avatar abs" role="img" aria-label="Customer portrait"></div>
<svg class="abs" style="left:727px;top:2676px" width="14" height="22" viewBox="0 0 14 22"><path d="M11 3L4 11l7 8" fill="none" stroke="#111" stroke-width="3"/></svg>
<svg class="abs" style="left:905px;top:2676px" width="14" height="22" viewBox="0 0 14 22"><path d="M3 3l7 8-7 8" fill="none" stroke="#29b6e6" stroke-width="3"/></svg>
<p class="testi-name abs serif">CLARA WHITFIELD</p>
<p class="testi-role abs">Actress</p>
<p class="testi-quote abs">"The Balance Diet is simple and it works! I am so grateful to have used the Balance Diet. So tasty and so healthy"</p>

<div class="ph" role="img" aria-label="Smiling man in a light blue shirt gesturing with an open hand" style="left:139px;top:2975px;width:416px;height:385px;background:linear-gradient(180deg,#fff 0%,#a9c9e6 45%,#3b3f46 100%)"></div>
<h2 class="q-title abs serif">Still have questions?</h2>
<p class="q-mail abs">Contact Us now at: hello@brightplate.ca</p>
<div class="btn" style="left:851px;top:3207px;width:196px;height:42px">Contact Now</div>

<footer>
  <div class="footer abs" role="img" aria-label="Dark blurred food background"></div>
  <h4 class="f-head abs" style="left:108px">ABOUT US</h4>
  <h4 class="f-head abs serif" style="left:436px;font-weight:400">QUICK LINKS</h4>
  <h4 class="f-head abs serif" style="left:612px;font-weight:400">CONTACT DETAILS</h4>
  <h4 class="f-head abs serif" style="left:865px;font-weight:400">QUICK INQUIRY</h4>
  <p class="f-about abs">The Balance Diet is based on 30% lean protein and the rest fruits and vegetables with a dash of Heart Healthy monounsaturated fats. Once these levels are reached and maintained, the body enters a state of hormonal balance which produces many positive effects, such as stable insulin and glucagon levels, increased energy, and weight loss.</p>
  <p class="f-love abs">Made with love by <b>BrightPlate.ca</b></p>
  <p class="f-team abs serif">The BrightPlate Meals Team</p>
  <ul class="f-links abs"><li>Home</li><li>How It Works</li><li>Pricing</li><li>Sample Menu</li><li>Celebrity</li><li>F.A.Q.</li><li>Contact Us</li></ul>
  <div class="f-contact abs">
    <b>BrightPlate Delivery Canada Inc.</b>
    <div class="f-row"><i></i><span>27-90 Harbour View Ave, Toronto, ON M4T 1K2</span></div>
    <div class="f-row"><i></i><span>416-555-0142</span></div>
    <b>BrightPlate Delivery LLC</b>
    <div class="f-row"><i></i><span>418 Maple Crest Road, Suite 300, Springfield, 10021</span></div>
    <div class="f-row"><i></i><span>416-555-0142</span></div>
    <div class="f-row"><i></i><span>hello@brightplate.ca</span></div>
  </div>
  <div class="inq abs" style="top:3488px">Name</div>
  <div class="inq abs" style="top:3524px">Email</div>
  <div class="inq abs" style="top:3560px;height:52px">Message</div>
  <div class="inq-btn abs">CONTACT NOW</div>
  <div class="bottom abs">Copyright © 2018 BrightPlate Meals. All Rights Reserved.</div>
  <div class="share abs"><span>Like</span><span>Share</span></div>
</footer>

</body>
</html>
```